I need a new business card design for my pharmacy.

I need a business card design. I will include my logo.
The card needs to be readable. I prefer to have my logo on one side along with my website, the other side includes the other information. Please use combination of black, neon green, white, and silver. This needs to catch the eye but yet be clearly visible and legible. Thanks

Industry/Entity Type

Pharmacy

Contact Information for Business Card

It needs to have the following information listed:
Mel's Apothecary Owner/Pharm D.
7134 North Brook Lane
Cedar Bend, MN 55921
Phone 555-318-6207
Fax 555-318-6209
email: mel@melsapothecary-example.com
www.melsapothecary-example.com
Store hours Monday-Friday 9 am- 6 pm
Saturday 9 am- 1 pm
Sunday Closed
Please utilize the colors black, white, and neon green, maybe silver.

Requirements
Must have
• It needs to be easily readable!
Nice to have
• It should catch the eye.
Should not have
• Do not use any other colors except listed: black, neon green, white, & silver.

```html
<!DOCTYPE html>
<html lang="en">
<head>
<meta charset="utf-8">
<title>Mel's Apothecary – Business Cards</title>
<link href="https://fonts.googleapis.com/css2?family=Open+Sans:wght@400;600&display=swap" rel="stylesheet">
<style>
  :root {
    --ink: #231f20;
    --band: #262324;
    --paper: #f4f4f4;
    --silver: #d9d9d9;
    --neon: #9ccb3b;
    --white: #ffffff;
    --backdrop: #e6e6e6;
  }
  * { margin: 0; padding: 0; box-sizing: border-box; }
  html, body { width: 1200px; height: 780px; overflow: hidden; }
  body {
    background: var(--backdrop);
    font-family: "Open Sans", sans-serif;
    position: relative;
  }
  .card {
    position: absolute;
    width: 525px;
    height: 300px;
    background: linear-gradient(135deg, var(--white), var(--paper) 60%, var(--silver));
    box-shadow: 0 6px 18px rgba(0,0,0,0.18);
    overflow: hidden;
  }
  .card--front { left: 50px; top: 80px; }
  .card--back { left: 625px; top: 400px; }

  .brand {
    position: absolute;
    display: flex;
    align-items: center;
  }
  .brand__mark {
    width: 34px; height: 34px;
    background: var(--neon);
  }
  .brand__divider {
    width: 1px; height: 62px;
    background: var(--ink);
    margin: 0 26px;
  }
  .brand__name {
    font-weight: 600;
    font-size: 40px;
    letter-spacing: -0.5px;
    color: var(--ink);
    white-space: nowrap;
  }
  .card--front .brand { left: 40px; top: 48px; }

  .info-band {
    position: absolute;
    left: 0; right: 0;
    top: 160px; height: 110px;
    background: var(--band);
    display: flex;
    align-items: center;
    padding: 0 28px;
    color: var(--white);
  }
  .owner { flex: 1; }
  .owner__name { font-size: 20px; font-weight: 600; line-height: 1.15; }
  .owner__title { font-size: 13px; color: var(--neon); margin-bottom: 4px; }
  .owner__address { font-size: 13px; line-height: 1.35; }
  .band-rule {
    width: 1px; height: 74px;
    background: var(--neon);
    margin: 0 18px;
  }
  .contact { list-style: none; font-size: 11.5px; line-height: 1; }
  .contact li { display: flex; align-items: center; margin: 4px 0; white-space: nowrap; }
  .contact svg { width: 13px; height: 13px; margin-right: 7px; flex: none; }

  .name-band {
    position: absolute;
    left: 0; right: 0;
    top: 45px; height: 120px;
    background: var(--band);
  }
  .name-band .brand { left: 40px; top: 29px; }
  .name-band .brand__divider { background: var(--white); }
  .name-band .brand__name { color: var(--white); }
  .hours {
    position: absolute;
    left: 40px; top: 190px;
    color: var(--ink);
    font-size: 13.5px;
    line-height: 1.45;
  }
  .hours__title { color: var(--neon); font-size: 17px; font-weight: 600; margin-bottom: 2px; }
</style>
</head>
<body>
  <section class="card card--front" aria-label="Business card front">
    <div class="brand">
      <span class="brand__mark"></span>
      <span class="brand__divider"></span>
      <span class="brand__name">Mel's Apothecary</span>
    </div>
    <div class="info-band">
      <div class="owner">
        <p class="owner__name">Mel's Apothecary</p>
        <p class="owner__title">Owner/Pharm D.</p>
        <p class="owner__address">7134 North Brook Lane<br>Cedar Bend, MN 55921</p>
      </div>
      <span class="band-rule"></span>
      <ul class="contact">
        <li>
          <svg viewBox="0 0 13 13" aria-hidden="true"><rect width="13" height="13" fill="var(--neon)"/><path d="M3.5 3h2l.6 2-1.1.8a5 5 0 0 0 2.2 2.2l.8-1.1 2 .6v2c-4 .3-6.8-2.5-6.5-6.5z" fill="var(--band)"/></svg>
          555-318-6207
        </li>
        <li>
          <svg viewBox="0 0 13 13" aria-hidden="true"><rect width="13" height="13" fill="var(--neon)"/><rect x="3" y="5" width="7" height="5" fill="var(--band)"/><rect x="4" y="2.5" width="5" height="2.5" fill="none" stroke="var(--band)"/></svg>
          555-318-6209
        </li>
        <li>
          <svg viewBox="0 0 13 13" aria-hidden="true"><rect width="13" height="13" fill="var(--neon)"/><rect x="2.5" y="3.5" width="8" height="6" fill="none" stroke="var(--band)"/><path d="M2.5 3.5l4 3.5 4-3.5" fill="none" stroke="var(--band)"/></svg>
          mel@melsapothecary-example.com
        </li>
        <li>
          <svg viewBox="0 0 13 13" aria-hidden="true"><rect width="13" height="13" fill="var(--neon)"/><circle cx="6.5" cy="6.5" r="4" fill="none" stroke="var(--band)"/><ellipse cx="6.5" cy="6.5" rx="1.8" ry="4" fill="none" stroke="var(--band)"/><path d="M2.5 6.5h8" stroke="var(--band)"/></svg>
          www.melsapothecary-example.com
        </li>
      </ul>
    </div>
  </section>

  <section class="card card--back" aria-label="Business card back">
    <div class="name-band">
      <div class="brand">
        <span class="brand__mark"></span>
        <span class="brand__divider"></span>
        <span class="brand__name">Mel's Apothecary</span>
      </div>
    </div>
    <div class="hours">
      <p class="hours__title">Store hours</p>
      <p>Monday-Friday 9 am- 6 pm | Saturday 9 am- 1 pm</p>
      <p>Sunday Closed</p>
    </div>
  </section>
</body>
</html>
```